Business card design for Velvet Harbor

We need business cards designed for our new marketing consulting company, Velvet Harbor. Our services include marketing strategy, go-to-market and launch planning, growth strategy, and execution. We serve medical technology and health technology companies, from startups to well-established growth companies.

The business cards should feel professional, credible, reliable and trustworthy, and should instill confidence. Also bold, creative, and modern.

The design must use the Velvet Harbor logo.

The primary brand color is this orange: #FF5501
A secondary color that you can use is this gray: #282B2D
I would prefer only to use the orange and gray. But if you feel you really need an additional accent color (please use it very sparingly, as little as possible), you can use this blue for small accent purposes: #009FED

Attached are the logo files. The main logo is the one with a little bit of orange on the left and the rest is gray.

The business card should include the following:

Velvet Harbor logo
First name and last name
Title
Email address
Phone number and type (in whatever order looks best for the design
Website (the website does not need to be in the same block as the personal info)

For example:

Nessa Pryle
Founder & Principal
nessa@velvetharbor.com
+1.628.309.4156 mobile (can use "." or spaces in between blocks of numbers)
velvetharbor.com (somewhere on the card, it does not need to be with the personal info; and note that there is no "www." at the beginning)

Note that there will be no address listed on the business card.

Target Market(s)

Executives (CEO, head of marketing, head of sales) at medical technology and health technology companies, mostly in their 40s and older, well-educated, often with advanced degrees. They are strategic thinkers, responsible for budgets, and familiar with P&L. Their comfort with and trust in using outside consultants varies.

Industry/Entity Type

Medical technology and health technology companies.

Contact Information for Business Card

See project description

Font styles to use
Sans Serif

Requirements
Must have
• Logo and see Business card details section above.

```html
<!DOCTYPE html>
<html lang="en">
<head>
<meta charset="UTF-8">
<title>Velvet Harbor — Business Card</title>
<link href="https://fonts.googleapis.com/css2?family=Exo+2:wght@400;500;700&display=swap" rel="stylesheet">
<style>
  :root {
    --orange: #FF5501;
    --graphite: #282B2D;
    --ink: #2E3133;
    --paper: #FFFFFF;
    --paper-shade: #EDEDED;
    --light-text: #E8E8E8;
    --stage: #E4E2DF;
  }
  * { box-sizing: border-box; margin: 0; padding: 0; }
  html, body {
    width: 1200px; height: 900px; overflow: hidden;
    background: var(--stage);
    font-family: "Exo 2", sans-serif;
  }
  .canvas { position: relative; width: 1200px; height: 900px; }

  .card {
    position: absolute; left: 320px;
    width: 560px; height: 320px;
    border-radius: 28px;
    overflow: hidden;
    box-shadow: 0 10px 28px rgba(0,0,0,0.18);
  }

  /* Back side */
  .card-back { top: 100px; background: var(--graphite); }
  .back-brand {
    position: absolute; left: 0; right: 0; top: 112px;
    display: flex; align-items: center; justify-content: center; gap: 10px;
    color: var(--light-text); font-weight: 500; font-size: 22px; letter-spacing: 0.04em;
  }
  .brand-dot { width: 12px; height: 12px; border-radius: 50%; background: var(--orange); }
  .back-rule {
    position: absolute; left: 70px; right: 70px; top: 178px;
    height: 1px; background: var(--orange);
  }
  .back-website {
    position: absolute; left: 0; right: 0; top: 192px;
    text-align: center; color: var(--light-text);
    font-size: 15px; letter-spacing: 0.55em;
  }

  /* Front side */
  .card-front {
    top: 480px;
    background: linear-gradient(115deg, var(--paper-shade) 0%, var(--paper) 55%, var(--paper) 100%);
  }
  .front-brand {
    position: absolute; left: 34px; top: 92px;
    display: flex; align-items: center; gap: 14px;
    color: var(--ink);
  }
  .front-brand .brand-dot { width: 16px; height: 16px; }
  .brand-name {
    font-weight: 700; font-size: 30px; line-height: 1.0;
    letter-spacing: 0.14em; text-transform: uppercase;
  }
  .contact {
    position: absolute; left: 318px; top: 178px;
    padding-left: 18px; border-left: 1px solid var(--ink);
    color: var(--ink);
  }
  .contact-name {
    color: var(--orange); font-weight: 700; font-size: 19px;
    text-transform: uppercase; letter-spacing: 0.01em; line-height: 1.1;
  }
  .contact-title { font-size: 14px; margin-top: 2px; }
  .contact-lines { list-style: none; margin-top: 14px; font-size: 13.5px; }
  .contact-lines li { display: flex; align-items: center; gap: 8px; line-height: 1.6; }
  .contact-lines svg { width: 14px; height: 14px; flex: none; }
</style>
</head>
<body>
<main class="canvas">

  <section class="card card-back" aria-label="Card back">
    <div class="back-brand"><span class="brand-dot"></span>Velvet Harbor</div>
    <div class="back-rule"></div>
    <p class="back-website">velvetharbor.com</p>
  </section>

  <section class="card card-front" aria-label="Card front">
    <div class="front-brand">
      <span class="brand-dot"></span>
      <span class="brand-name">Velvet<br>Harbor</span>
    </div>

    <div class="contact">
      <p class="contact-name">Nessa Pryle</p>
      <p class="contact-title">Founder &amp; Principal</p>
      <ul class="contact-lines">
        <li>
          <svg viewBox="0 0 24 24" aria-hidden="true"><path fill="#FF5501" d="M6.6 10.8a15.1 15.1 0 0 0 6.6 6.6l2.2-2.2a1 1 0 0 1 1-.25 11.4 11.4 0 0 0 3.6.57 1 1 0 0 1 1 1V20a1 1 0 0 1-1 1A17 17 0 0 1 3 4a1 1 0 0 1 1-1h3.5a1 1 0 0 1 1 1c0 1.25.2 2.45.57 3.57a1 1 0 0 1-.25 1z"/></svg>
          +1.628.309.4156
        </li>
        <li>
          <svg viewBox="0 0 24 24" aria-hidden="true"><path fill="#FF5501" d="M2 5h20v14H2z"/><path fill="none" stroke="#FFFFFF" stroke-width="1.6" d="M2.5 5.5 12 13l9.5-7.5"/></svg>
          nessa@velvetharbor.com
        </li>
      </ul>
    </div>
  </section>

</main>
</body>
</html>
```